依頼詳細
お客様にわかりやすく、またチラシをみてポイントカードを持っておきたい、もらっておきたいと思わせるデザインを希望します。お客様の目に入りやすく、A1のポスターや、レジ横でA4の用紙に置く予定です。
内容はジュース1杯で1P
10Pでお好きなドリンク1杯サービスです!(どのサイズでも)
入会費、年会費無料、有効期限なし!
記載項目
ポイントカード
サイズ
A4
ページ数
片面
希望イメージ
シンプル 複雑
単色 カラフル
暗い 明るい
日常 高級
遊び心 厳粛
未来的 伝統的
女性的 男性的
希望する色
黄・オレンジ系
納品ファイル
• 高解像度JPG (.jpg)
補足説明
参考イメージ添付します。
依頼公開後の追記内容
ポイントカード画像を添付します。
■ 選んだ理由

ポイントカードが目立つ

■ 提案者全員のお礼・コメント

どれもレベルが高い提案で選ぶことが難しかったです。また機会がございましたらよろしくお願いします。

```html
<!DOCTYPE html>
<html lang="ja">
<head>
<meta charset="UTF-8">
<title>ポイントカードde お得に贅沢</title>
<link rel="stylesheet" href="https://fonts.googleapis.com/css2?family=M+PLUS+Rounded+1c:wght@500;800;900&family=Noto+Sans+JP:wght@400;700;900&display=swap">
<style>
:root{
  --orange:#f47a1f;
  --orange-deep:#e85a0c;
  --orange-light:#fbb066;
  --cream:#fff3e4;
  --card-yellow:#f9eb92;
  --card-edge:#e5c75b;
  --red:#e8261a;
  --ink:#3a2a20;
  --white:#ffffff;
  --lilac:#f3e6f7;
  --lilac-edge:#c9a4d8;
}
*{margin:0;padding:0;box-sizing:border-box}
html,body{width:849px;height:1200px;overflow:hidden;background:var(--white)}
.poster{
  position:relative;width:849px;height:1200px;overflow:hidden;
  font-family:"Noto Sans JP",sans-serif;color:var(--ink);
  background:radial-gradient(ellipse 70% 45% at 50% 35%,var(--cream) 0%,var(--orange-light) 55%,var(--orange) 100%);
}
.mango-photo{
  position:absolute;left:0;top:660px;width:849px;height:418px;
  background:radial-gradient(ellipse 60% 70% at 55% 60%,#ffb347 0%,#f7941d 45%,#e06a10 100%);
}
.title-main{
  position:absolute;left:46px;top:66px;white-space:nowrap;
  font-family:"M PLUS Rounded 1c",sans-serif;font-weight:900;font-size:88px;letter-spacing:-3px;
  color:var(--white);-webkit-text-stroke:10px var(--orange-deep);paint-order:stroke fill;
  line-height:1;
}
.title-de{
  position:absolute;left:696px;top:106px;line-height:1;
  font-family:"M PLUS Rounded 1c",sans-serif;font-weight:800;font-size:46px;color:var(--ink);
}
.title-sub{
  position:absolute;left:520px;top:200px;line-height:1.2;
  font-family:"M PLUS Rounded 1c",sans-serif;font-weight:800;font-size:56px;color:var(--ink);letter-spacing:2px;
}
.point-card{
  position:absolute;width:240px;height:165px;background:var(--card-yellow);
  border:2px solid var(--card-edge);box-shadow:4px 6px 10px rgba(120,60,0,.25);
}
.point-card.front{left:158px;top:305px;transform:rotate(-1deg)}
.point-card.back{left:430px;top:318px;transform:rotate(2.5deg)}
.recruit{
  position:absolute;left:0;top:572px;width:849px;text-align:center;
  font-family:"M PLUS Rounded 1c",sans-serif;font-weight:900;font-size:50px;letter-spacing:4px;
  color:var(--white);-webkit-text-stroke:8px var(--orange-deep);paint-order:stroke fill;
}
.benefits{
  position:absolute;left:50px;top:730px;width:306px;height:292px;
  background:rgba(255,255,255,.55);border-radius:10px;padding:22px 16px;
  display:flex;flex-direction:column;justify-content:space-between;
}
.benefits li{
  list-style:none;background:var(--lilac);border:2px solid var(--lilac-edge);border-radius:6px;
  padding:10px 12px;font-weight:700;font-size:21px;color:var(--ink);
}
.benefits li::before{content:"・";color:var(--orange-deep)}
.arrow{position:absolute;left:360px;top:798px}
.reward{
  position:absolute;left:476px;top:732px;width:346px;height:276px;
  background:var(--white);border-radius:14px;transform:rotate(-3deg);
  box-shadow:3px 5px 10px rgba(120,60,0,.3);
  text-align:center;font-family:"M PLUS Rounded 1c",sans-serif;font-weight:800;
  padding-top:18px;color:var(--ink);
}
.reward .pts{
  display:inline-block;background:var(--orange);color:var(--white);
  border-radius:30px;padding:0 18px;font-size:34px;line-height:48px;
}
.reward .de{font-size:28px}
.reward .line{display:block;font-size:30px;line-height:1.35}
.reward .free{display:block;margin-top:6px;font-size:58px;font-weight:900;color:var(--red);line-height:1.1}
.notes{
  position:absolute;left:0;top:1078px;width:849px;height:122px;background:var(--white);
  padding:16px 40px;font-size:12px;line-height:1.6;color:var(--ink);list-style:none;
}
</style>
</head>
<body>
<main class="poster">
  <div class="mango-photo" role="img" aria-label="カットされた完熟マンゴーの写真"></div>

  <h1>
    <span class="title-main">ポイントカード</span>
    <span class="title-de">de</span>
    <span class="title-sub">お得に贅沢</span>
  </h1>

  <div class="point-card front" role="img" aria-label="ポイントカード表面"></div>
  <div class="point-card back" role="img" aria-label="ポイントカード裏面"></div>

  <p class="recruit">〜新規会員様募集中〜</p>

  <ul class="benefits">
    <li>入会費・年会費無料</li>
    <li>有効期限なし</li>
    <li>ドリンク1杯につき1P</li>
    <li>10Pごとに嬉しい特典</li>
  </ul>

  <svg class="arrow" width="108" height="140" viewBox="0 0 108 140" aria-hidden="true">
    <path d="M0 38 H52 V0 L108 70 L52 140 V102 H0 Z" fill="#e8261a"/>
  </svg>

  <div class="reward">
    <span class="pts">10P</span><span class="de">で</span>
    <span class="line">選べるサイズの</span>
    <span class="line">お好きなドリンクが</span>
    <span class="free">1杯無料!</span>
  </div>

  <ul class="notes">
    <li>○ドリンク1杯のご購入につき、1ポイントを贈します。</li>
    <li>○1名様で1枚のポイントカード発行とし、複数名様ご購入で一括払いの場合は、人数分のポイントカードを発行いたします。</li>
    <li>○入会費・年会費は一切かかりません。</li>
    <li>○有効期限はございません。</li>
  </ul>
</main>
</body>
</html>
```